Saffron Lantern Court Business Card

I am looking for a business card desgined for my restaurant. It is an Indian restaurant, we are looking for something thats modern, yet traditional with the indian culture, we are looking for colors that match our logo. The logo is a design of the building with the name of the restaurant. for more information on the restaurant go to www.saffronlanterncourt.example

Industry/Entity Type

Indian Restaurant

Contact Information for Business Card

we are looking for somthing thats modern, yet traditional with the indian culture, we are looking for colors that match our logo. The logo is a design of the building with the name of the restaurant. for more information on the restaurant go to www.saffronlanterncourt.example

Requirements
Must have
• The logo that is attached,
• Name: Harvinder Oberoi,
• address of the restaurant: 7328 West Larkspur Rd, Phoenix, Arizona, 85213
• Phone: (602) 555-0147
• Fax: (602) 555-0193
• Restaurant Catering Banquet
• Website: www.SaffronLanternCourt.example
Nice to have
• wanted to get something that goes with the theme of the restaurant, which is traditional but also keep a very professional and modern touch

```html
<!DOCTYPE html>
<html lang="en">
<head>
<meta charset="utf-8">
<title>Saffron Lantern Court Business Card</title>
<link rel="stylesheet" href="https://fonts.googleapis.com/css2?family=Montserrat:wght@400;600;700&display=swap">
<style>
  :root {
    --stage: #2b2b2b;
    --card: #050505;
    --saffron: #f07a1e;
    --ember: #e2572a;
    --ink-light: #f4f4f4;
    --rule: #e6e6e6;
  }
  * { margin: 0; padding: 0; box-sizing: border-box; }
  html, body { width: 1200px; height: 900px; overflow: hidden; }
  body {
    background: var(--stage);
    font-family: "Montserrat", Arial, sans-serif;
    position: relative;
  }
  .card {
    position: absolute;
    width: 700px;
    height: 400px;
    background: var(--card);
    border-radius: 22px;
    overflow: hidden;
  }
  .card--front { left: 110px; top: 30px; }
  .card--back { left: 390px; top: 470px; }

  .brand-name {
    color: var(--ember);
    font-weight: 700;
    text-transform: uppercase;
    line-height: 1.08;
    letter-spacing: 2px;
    text-align: center;
  }
  .card--front .brand-name {
    position: absolute;
    left: 0; right: 0;
    top: 100px;
    font-size: 46px;
  }
  .website {
    color: var(--ink-light);
    font-weight: 400;
    white-space: nowrap;
  }
  .website strong { color: var(--saffron); font-weight: 700; }
  .card--front .website {
    position: absolute;
    left: 0; right: 0;
    bottom: 44px;
    text-align: center;
    font-size: 20px;
  }

  .card--back .brand-name {
    position: absolute;
    left: 60px;
    top: 44px;
    width: 220px;
    font-size: 28px;
  }
  .name-rule {
    position: absolute;
    left: 0; right: 0;
    top: 218px;
    display: flex;
    align-items: center;
    gap: 10px;
  }
  .name-rule .line {
    height: 2px;
    background: var(--rule);
  }
  .name-rule .line--lead { width: 140px; flex: none; }
  .name-rule .line--trail { flex: 1; }
  .holder-name {
    color: var(--saffron);
    font-size: 24px;
    font-weight: 700;
    letter-spacing: 1px;
    text-transform: uppercase;
    white-space: nowrap;
  }
  .contact {
    position: absolute;
    left: 420px;
    top: 92px;
    color: var(--ink-light);
    font-size: 14px;
    line-height: 1.5;
    list-style: none;
  }
  .contact li { display: flex; align-items: center; gap: 8px; white-space: nowrap; }
  .contact .icon { width: 12px; height: 12px; flex: none; }
  .contact .website { font-size: 14px; }
</style>
</head>
<body>
  <section class="card card--front">
    <p class="brand-name">Saffron<br>Lantern<br>Court</p>
    <p class="website">www.<strong>SaffronLanternCourt</strong>.example</p>
  </section>

  <section class="card card--back">
    <p class="brand-name">Saffron<br>Lantern<br>Court</p>
    <ul class="contact">
      <li>7328 West Larkspur Rd</li>
      <li>Phoenix, Arizona, 85213</li>
      <li>
        <svg class="icon" viewBox="0 0 24 24" aria-hidden="true"><path fill="#f07a1e" d="M6.6 10.8a15.1 15.1 0 0 0 6.6 6.6l2.2-2.2a1 1 0 0 1 1-.25 11.4 11.4 0 0 0 3.6.57 1 1 0 0 1 1 1V20a1 1 0 0 1-1 1A17 17 0 0 1 3 4a1 1 0 0 1 1-1h3.5a1 1 0 0 1 1 1c0 1.25.2 2.45.57 3.57a1 1 0 0 1-.25 1z"/></svg>
        (602) 555-0147
      </li>
      <li>
        <svg class="icon" viewBox="0 0 24 24" aria-hidden="true"><rect x="6" y="3" width="12" height="6" fill="#f07a1e"/><rect x="3" y="10" width="18" height="8" rx="2" fill="#f07a1e"/><rect x="7" y="15" width="10" height="6" fill="#f07a1e"/></svg>
        (602) 555-0193
      </li>
      <li>
        <svg class="icon" viewBox="0 0 24 24" aria-hidden="true"><circle cx="12" cy="12" r="9" fill="none" stroke="#f07a1e" stroke-width="2.4"/><path d="M3 12h18M12 3c3 3 3 15 0 18M12 3c-3 3-3 15 0 18" fill="none" stroke="#f07a1e" stroke-width="1.8"/></svg>
        <span class="website">www.<strong>SaffronLanternCourt</strong>.example</span>
      </li>
    </ul>
    <div class="name-rule">
      <span class="line line--lead"></span>
      <p class="holder-name">Harvinder Oberoi</p>
      <span class="line line--trail"></span>
    </div>
  </section>
</body>
</html>
```